World travel poster - I want to remember where I've been!

I would like a poster for me to print and keep in my home as a record of my world travels. It must look like a mechanical sign in an airport (see picture for example) However I am flexible with exact layout, if you'd like to add images used to enhance poster etc. I have also uploaded some pictures from my travels if you would like to use some or all of them. They are named according to location.

Poster must include:
USA 2003
Malaysia 2006
Thailand 2007
Italy 2009
India, Vietnam, Hong Kong 2010
Bali 2011
Malaysia 2012
Singapore 2012
Vietnam, Cambodia, Laos 2013
Europe 2015

and the quote:

"The world is a book and those who do not travel read only one page."
― Corwin of Veldmarsh
Updates

Hi there. I have uploaded some photos of my travels to possibly use in my poster. They are named according to location. I haven't decided if I prefer the originial layout or with images, so please post both for me to consider. Thanks so much for your time to consider my project.

Target Market(s)

Something to catch the eye of visitors and remind me of my adventures.
A classic piece that is a conversation starter.

Industry/Entity Type

Airport

Font styles to use
Other font styles liked:
• Airport mechanical font

Requirements
Must have
• Some lettering like a mechanical airport board (see image attached for example).
Dimensions that are easy to print - either A3, or a long/narrow poster.
Nice to have
• A splash of colour or an image, maybe the words 'arrivals' or 'departures'

Use of some of my pictures if it doesn't look too busy.
Should not have
• Anything too over the top.

```html
<!DOCTYPE html>
<html lang="en">
<head>
<meta charset="utf-8">
<title>World Travel Departures Board</title>
<link href="https://fonts.googleapis.com/css2?family=Oswald:wght@500&family=Open+Sans:ital,wght@1,300;1,400&display=swap" rel="stylesheet">
<style>
  :root {
    --page-bg: #f2f2f2;
    --board-bg: #111111;
    --tile-top: #2b2b2b;
    --tile-bottom: #161616;
    --tile-split: #050505;
    --tile-text: #f4f4f4;
    --year-top: #ffd62a;
    --year-bottom: #e9b300;
    --year-text: #141414;
    --quote-text: #c9c9c9;
    --rule: #2a2a2a;
  }
  * { box-sizing: border-box; margin: 0; padding: 0; }
  html, body {
    width: 1200px;
    height: 900px;
    overflow: hidden;
    background: var(--page-bg);
  }
  .poster {
    position: absolute;
    left: 400px;
    top: 50px;
    width: 400px;
    height: 800px;
    background: var(--board-bg);
    padding: 22px 16px 0 18px;
  }
  .board { display: flex; flex-direction: column; gap: 6px; }
  .row { display: flex; gap: 2px; height: 40px; }
  .tile {
    position: relative;
    width: 24px;
    height: 40px;
    border-radius: 3px;
    background: linear-gradient(var(--tile-top), var(--tile-bottom));
    box-shadow: inset 0 1px 0 rgba(255,255,255,0.08), 0 1px 2px rgba(0,0,0,0.8);
    color: var(--tile-text);
    font-family: "Oswald", "Arial Narrow", sans-serif;
    font-weight: 500;
    font-size: 30px;
    line-height: 40px;
    text-align: center;
  }
  .tile::after {
    content: "";
    position: absolute;
    left: 0; right: 0; top: 50%;
    height: 1px;
    background: var(--tile-split);
    opacity: 0.85;
  }
  .year { display: flex; gap: 2px; margin-left: 2px; }
  .year .tile {
    background: linear-gradient(var(--year-top), var(--year-bottom));
    color: var(--year-text);
  }
  .year .tile::before {
    content: "";
    position: absolute;
    left: -3px; right: -3px; top: calc(50% - 2px);
    height: 4px;
    background:
      radial-gradient(circle, #222 1.5px, transparent 2px) left center / 4px 4px no-repeat,
      radial-gradient(circle, #222 1.5px, transparent 2px) right center / 4px 4px no-repeat;
    z-index: 1;
  }
  .year .tile::after { background: rgba(0,0,0,0.55); }
  .quote {
    margin: 38px 8px 0 14px;
    padding: 12px 12px 14px;
    border-top: 1px solid var(--rule);
    border-bottom: 1px solid var(--rule);
    color: var(--quote-text);
    font-family: "Open Sans", Arial, sans-serif;
  }
  .quote-text {
    font-style: italic;
    font-weight: 300;
    font-size: 12.5px;
    line-height: 1.5;
    letter-spacing: 0.3px;
    text-transform: uppercase;
  }
  .quote-author {
    margin-top: 4px;
    font-size: 8px;
    letter-spacing: 0.4px;
    text-transform: uppercase;
  }
</style>
</head>
<body>
<main class="poster">
  <div class="board">
    <div class="row"><span class="tile">U</span><span class="tile">S</span><span class="tile">A</span><span class="tile"></span><span class="tile"></span><span class="tile"></span><span class="tile"></span><span class="tile"></span><span class="tile"></span><span class="tile"></span><span class="year"><span class="tile">2</span><span class="tile">0</span><span class="tile">0</span><span class="tile">3</span></span></div>
    <div class="row"><span class="tile">M</span><span class="tile">A</span><span class="tile">L</span><span class="tile">A</span><span class="tile">Y</span><span class="tile">S</span><span class="tile">I</span><span class="tile">A</span><span class="tile"></span><span class="tile"></span><span class="year"><span class="tile">2</span><span class="tile">0</span><span class="tile">0</span><span class="tile">6</span></span></div>
    <div class="row"><span class="tile">T</span><span class="tile">H</span><span class="tile">A</span><span class="tile">I</span><span class="tile">L</span><span class="tile">A</span><span class="tile">N</span><span class="tile">D</span><span class="tile"></span><span class="tile"></span><span class="year"><span class="tile">2</span><span class="tile">0</span><span class="tile">0</span><span class="tile">7</span></span></div>
    <div class="row"><span class="tile">I</span><span class="tile">T</span><span class="tile">A</span><span class="tile">L</span><span class="tile">Y</span><span class="tile"></span><span class="tile"></span><span class="tile"></span><span class="tile"></span><span class="tile"></span><span class="year"><span class="tile">2</span><span class="tile">0</span><span class="tile">0</span><span class="tile">9</span></span></div>
    <div class="row"><span class="tile">I</span><span class="tile">N</span><span class="tile">D</span><span class="tile">I</span><span class="tile">A</span><span class="tile"></span><span class="tile"></span><span class="tile"></span><span class="tile"></span><span class="tile"></span><span class="year"><span class="tile">2</span><span class="tile">0</span><span class="tile">1</span><span class="tile">0</span></span></div>
    <div class="row"><span class="tile">V</span><span class="tile">I</span><span class="tile">E</span><span class="tile">T</span><span class="tile">N</span><span class="tile">A</span><span class="tile">M</span><span class="tile"></span><span class="tile"></span><span class="tile"></span><span class="year"><span class="tile">2</span><span class="tile">0</span><span class="tile">1</span><span class="tile">0</span></span></div>
    <div class="row"><span class="tile">H</span><span class="tile">O</span><span class="tile">N</span><span class="tile">G</span><span class="tile"></span><span class="tile">K</span><span class="tile">O</span><span class="tile">N</span><span class="tile">G</span><span class="tile"></span><span class="year"><span class="tile">2</span><span class="tile">0</span><span class="tile">1</span><span class="tile">0</span></span></div>
    <div class="row"><span class="tile">B</span><span class="tile">A</span><span class="tile">L</span><span class="tile">I</span><span class="tile"></span><span class="tile"></span><span class="tile"></span><span class="tile"></span><span class="tile"></span><span class="tile"></span><span class="year"><span class="tile">2</span><span class="tile">0</span><span class="tile">1</span><span class="tile">1</span></span></div>
    <div class="row"><span class="tile">M</span><span class="tile">A</span><span class="tile">L</span><span class="tile">A</span><span class="tile">Y</span><span class="tile">S</span><span class="tile">I</span><span class="tile">A</span><span class="tile"></span><span class="tile"></span><span class="year"><span class="tile">2</span><span class="tile">0</span><span class="tile">1</span><span class="tile">2</span></span></div>
    <div class="row"><span class="tile">S</span><span class="tile">I</span><span class="tile">N</span><span class="tile">G</span><span class="tile">A</span><span class="tile">P</span><span class="tile">O</span><span class="tile">R</span><span class="tile">E</span><span class="tile"></span><span class="year"><span class="tile">2</span><span class="tile">0</span><span class="tile">1</span><span class="tile">2</span></span></div>
    <div class="row"><span class="tile">V</span><span class="tile">I</span><span class="tile">E</span><span class="tile">T</span><span class="tile">N</span><span class="tile">A</span><span class="tile">M</span><span class="tile"></span><span class="tile"></span><span class="tile"></span><span class="year"><span class="tile">2</span><span class="tile">0</span><span class="tile">1</span><span class="tile">3</span></span></div>
    <div class="row"><span class="tile">C</span><span class="tile">A</span><span class="tile">M</span><span class="tile">B</span><span class="tile">O</span><span class="tile">D</span><span class="tile">I</span><span class="tile">A</span><span class="tile"></span><span class="tile"></span><span class="year"><span class="tile">2</span><span class="tile">0</span><span class="tile">1</span><span class="tile">3</span></span></div>
    <div class="row"><span class="tile">L</span><span class="tile">A</span><span class="tile">O</span><span class="tile">S</span><span class="tile"></span><span class="tile"></span><span class="tile"></span><span class="tile"></span><span class="tile"></span><span class="tile"></span><span class="year"><span class="tile">2</span><span class="tile">0</span><span class="tile">1</span><span class="tile">3</span></span></div>
    <div class="row"><span class="tile">E</span><span class="tile">U</span><span class="tile">R</span><span class="tile">O</span><span class="tile">P</span><span class="tile">E</span><span class="tile"></span><span class="tile"></span><span class="tile"></span><span class="tile"></span><span class="year"><span class="tile">2</span><span class="tile">0</span><span class="tile">1</span><span class="tile">5</span></span></div>
  </div>
  <blockquote class="quote">
    <p class="quote-text">"The world is a book and those who do not travel read only one page."</p>
    <p class="quote-author">— Corwin of Veldmarsh</p>
  </blockquote>
</main>
</body>
</html>
```